Website wordpress theme for brightwillowstudio.au

We need a modern dark mode website to entice customers to engage us to deliver web apps, mobile apps and VR apps. The site emphasises humans over tech.

Target Market(s)

Medium to large business and well funded startups

Industry/Entity Type

Information Technology

Coding

Coded - Design and coding required

Font styles to use
Sans Serif

Colors
EB3D1F
EC4F4E
F09395
F8D3D4
FCEDEE

Requirements
Must have
• Attractive image on home page

```html
<!DOCTYPE html>
<html lang="en">
<head>
<meta charset="utf-8">
<title>Bright Willow Studio</title>
<link href="https://fonts.googleapis.com/css2?family=Poppins:wght@400;500;600;700&display=swap" rel="stylesheet">
<style>
:root{
  --red:#EB3D1F;
  --red-soft:#EC4F4E;
  --pink:#F09395;
  --blush:#F8D3D4;
  --mist:#FCEDEE;
  --ink:#0a0b0f;
  --night:#111318;
  --white:#ffffff;
  --grey:#c9ccd3;
}
*{margin:0;padding:0;box-sizing:border-box}
html,body{width:1200px;height:3784px;overflow:hidden;background:var(--ink);font-family:'Poppins',sans-serif;color:var(--white)}
.page{position:relative;width:1200px;height:3784px}
.section{position:absolute;left:0;width:1200px;overflow:hidden}
.fill{position:absolute;inset:0}
.btn{display:inline-block;background:var(--red);color:var(--white);font-weight:600;font-size:13px;text-transform:uppercase;padding:8px 22px;border-radius:20px;letter-spacing:.5px;white-space:nowrap}
.link{font-size:13px;font-weight:600;text-transform:uppercase;color:var(--white);letter-spacing:.5px}
.link::after{content:" »";color:var(--red)}
p{font-size:15px;line-height:1.65;color:var(--grey)}

/* header */
.hero{top:0;height:680px}
.hero .fill{background:radial-gradient(circle at 62% 35%,#5a7fa8 0%,#1d3550 22%,#0c1522 55%,#05080d 100%)}
.nav{position:absolute;top:14px;left:28px;right:90px;display:flex;align-items:center}
.brand{display:flex;align-items:center;gap:10px;font-size:22px;font-weight:700;color:var(--white)}
.brand i{width:18px;height:18px;background:var(--red);display:block}
.menu{margin-left:auto;display:flex;gap:40px;align-items:center;font-size:14px;font-weight:500}
.menu .on{color:var(--red)}
.hero-title{position:absolute;left:120px;top:282px;font-size:34px;font-weight:700}
.hero-text{position:absolute;left:120px;top:332px;width:420px;font-size:14px;color:var(--white)}
.hero-cta{position:absolute;left:120px;top:406px}
.arrow{position:absolute;top:360px}
.dots{position:absolute;top:640px;left:565px;display:flex;gap:10px}
.dots span{width:10px;height:10px;border-radius:50%;background:#666}
.dots span:first-child{background:var(--white)}

/* welcome */
.welcome{top:680px;height:510px;background:var(--ink)}
.welcome .art{position:absolute;left:130px;top:50px;width:390px;height:390px;background:linear-gradient(135deg,#2a3a52,#0e1626);border-radius:8px}
.welcome .kicker{position:absolute;left:625px;top:100px;color:var(--red);font-size:15px;font-weight:600;text-transform:uppercase}
.welcome h2{position:absolute;left:625px;top:118px;font-size:28px;font-weight:700}
.welcome h2::before{content:"";position:absolute;left:-20px;top:-24px;width:4px;height:70px;background:var(--red)}
.welcome p{position:absolute;left:625px;top:168px;width:470px}
.welcome .link{position:absolute;left:632px;top:392px}

/* services */
.service .inner{position:absolute;left:0;right:0;text-align:center}
.service h2{font-size:38px;font-weight:700}
.service p{width:640px;margin:8px auto 14px;color:var(--white)}
.web{top:1190px;height:510px}
.web .fill{background:linear-gradient(90deg,#0c1d3a 0%,#15335c 40%,#0e1a2c 70%,#2c2a2e 100%)}
.mobile{top:1700px;height:490px}
.mobile .fill{background:linear-gradient(90deg,#3a342e 0%,#2b2a2c 45%,#3b5060 75%,#2a3642 100%)}
.vr{top:2190px;height:510px}
.vr .fill{background:linear-gradient(90deg,#3b4048 0%,#2d3139 45%,#16181d 70%,#2a2c31 100%)}
.shade{position:absolute;inset:0;background:rgba(0,0,0,.35)}

/* blog */
.blog{top:2700px;height:570px;background:var(--night)}
.blog h2{position:absolute;top:60px;width:100%;text-align:center;font-size:32px;font-weight:700}
.card{position:absolute;top:130px;width:320px;text-align:center}
.card .thumb{height:160px;border-radius:2px}
.card h3{font-size:19px;font-weight:600;line-height:1.35;margin:22px 0 8px}
.card p{font-size:13px;line-height:1.5;margin-bottom:14px}

/* footer */
.footer{top:3270px;height:514px}
.footer .fill{background:linear-gradient(180deg,#0d0f14 0%,#181a22 60%,#221618 100%)}
.col{position:absolute;left:100px;top:82px}
.col h4{font-size:15px;font-weight:600;margin-bottom:6px}
.col p{font-size:13px;line-height:1.6;margin-bottom:20px}
.col u{color:var(--grey)}
.contact{position:absolute;left:445px;top:70px;width:655px;height:370px}
.contact h2{font-size:30px;font-weight:700}
.field{position:absolute;border-bottom:1px solid #6b6f78;font-size:12px;color:var(--grey);padding-bottom:18px}
.submit{position:absolute;left:0;top:318px}
.social{position:absolute;right:90px;top:462px;display:flex;gap:14px}
.social span{width:28px;height:28px;border-radius:50%;background:var(--red)}
.copy{position:absolute;left:100px;top:470px;font-size:13px;color:var(--grey)}
</style>
</head>
<body>
<div class="page">

<header class="section hero">
  <div class="fill" role="img" aria-label="Robotic hand reaching toward a human hand beneath a glowing lightbulb"></div>
  <nav class="nav">
    <div class="brand"><i></i>Bright Willow Studio</div>
    <div class="menu">
      <span class="on">Home</span><span>About</span><span>Our Services</span><span>Blog</span>
      <span class="btn">Contact Us »</span>
    </div>
  </nav>
  <h1 class="hero-title">Bright Willow Studio</h1>
  <p class="hero-text">Lorem ipsum dolor sit amet, consectetur adipiscing elit, sed do eiusmod tempor incididunt ut labore et dolore magna aliqua.</p>
  <span class="btn hero-cta">Get Started »</span>
  <svg class="arrow" style="left:48px" width="24" height="34" viewBox="0 0 24 34"><path d="M18 3 4 17l14 14" stroke="#fff" stroke-width="3" fill="none"/></svg>
  <svg class="arrow" style="left:1126px" width="24" height="34" viewBox="0 0 24 34"><path d="M6 3l14 14L6 31" stroke="#fff" stroke-width="3" fill="none"/></svg>
  <div class="dots"><span></span><span></span><span></span><span></span></div>
</header>

<section class="section welcome">
  <div class="art" role="img" aria-label="Person working on a laptop framed in a large X shape"></div>
  <span class="kicker">Welcome to</span>
  <h2>Bright Willow Studio</h2>
  <p>Lorem ipsum dolor sit amet, consectetur adipiscing elit, sed do eiusmod tempor incididunt ut labore et dolore magna aliqua. Quis ipsum suspendisse ultrices gravida risus commodo viverra maecenas accumsan lacus vel facilisis. Sed ut perspiciatis unde omnis iste natus error sit voluptatem accusantium doloremque laudantium, totam rem aperiam, eaque ipsa quae ab illo inventore veritatis.</p>
  <span class="link">Learn more about us</span>
</section>

<section class="section service web">
  <div class="fill" role="img" aria-label="Developer looking at monitors full of code"></div><div class="shade"></div>
  <div class="inner" style="top:90px">
    <h2>Web Apps</h2>
    <p>Lorem ipsum dolor sit amet, consectetur adipiscing elit, sed do eiusmod tempor incididunt ut labore et dolore magna aliqua. Quis ipsum suspendisse ultrices gravida risus commodo viverra maecenas accumsan lacus.</p>
    <span class="link">Learn more</span>
  </div>
</section>

<section class="section service mobile">
  <div class="fill" role="img" aria-label="Two colleagues reviewing a phone app beside screens of wireframes"></div><div class="shade"></div>
  <div class="inner" style="top:60px">
    <h2>Mobile Apps</h2>
    <p>Lorem ipsum dolor sit amet, consectetur adipiscing elit, sed do eiusmod tempor incididunt ut labore et dolore magna aliqua. Quis ipsum suspendisse ultrices gravida risus commodo viverra maecenas.</p>
    <span class="link">Learn more</span>
  </div>
</section>

<section class="section service vr">
  <div class="fill" role="img" aria-label="Person using a virtual reality headset with hand controllers"></div><div class="shade"></div>
  <div class="inner" style="top:60px">
    <h2>VR Apps</h2>
    <p>Lorem ipsum dolor sit amet, consectetur adipiscing elit, sed do eiusmod tempor incididunt ut labore et dolore magna aliqua. Quis ipsum suspendisse ultrices gravida risus commodo viverra maecenas.</p>
    <span class="link">Learn more</span>
  </div>
</section>

<section class="section blog">
  <h2>Latest Blog</h2>
  <article class="card" style="left:95px">
    <div class="thumb" role="img" aria-label="Engineer working with a robotic arm" style="background:linear-gradient(135deg,#2d5a70,#0e1e2c)"></div>
    <h3>The standard Lorem Ipsum pass used since the 1500s</h3>
    <p>Sed ut perspiciatis unde omnis iste natus error accusantium doloremque</p>
    <span class="link">Learn more</span>
  </article>
  <article class="card" style="left:440px">
    <div class="thumb" role="img" aria-label="Woman working at a computer in a dark office" style="background:linear-gradient(135deg,#3a3f4a,#121419)"></div>
    <h3>The standard Lorem Ipsum pass used since the 1500s</h3>
    <p>Sed ut perspiciatis unde omnis iste natus error accusantium doloremque</p>
    <span class="link">Learn more</span>
  </article>
  <article class="card" style="left:785px">
    <div class="thumb" role="img" aria-label="Programmer at a desk with several monitors" style="background:linear-gradient(135deg,#4a4d55,#1a1c22)"></div>
    <h3>The standard Lorem Ipsum pass used since the 1500s</h3>
    <p>Sed ut perspiciatis unde omnis iste natus error accusantium doloremque</p>
    <span class="link">Learn more</span>
  </article>
</section>

<footer class="section footer">
  <div class="fill" role="img" aria-label="Night city skyline fading into dark background"></div>
  <div class="col">
    <h4>Find Us</h4>
    <p>1234 Main Rd<br>Somewhere, US 12345</p>
    <h4>Find Us</h4>
    <p>+1 888-888-8888<br>info@brightwillowstudio.au</p>
    <h4>Legal Stuff</h4>
    <p><u>Privacy Policy</u><br><u>Terms &amp; Conditions</u></p>
  </div>
  <div class="contact">
    <h2>Contact Us</h2>
    <div class="field" style="left:0;top:62px;width:310px">Enter Your Name</div>
    <div class="field" style="left:345px;top:62px;width:310px">Enter Your Email</div>
    <div class="field" style="left:0;top:122px;width:310px">Enter Your Number</div>
    <div class="field" style="left:345px;top:122px;width:310px">Country</div>
    <div class="field" style="left:0;top:182px;width:655px;height:110px">Enter Your Message here</div>
    <span class="btn submit">Submit Now »</span>
  </div>
  <div class="social"><span></span><span></span><span></span><span></span></div>
  <div class="copy">©Copyright 2022 brightwillowstudio. All Rights Reserved.</div>
</footer>

</div>
</body>
</html>
```